Business Card for a Wedding Films Business

We require a business card design for our business 'Lewis Barnow Wedding Films'. The logo needs to look classy and high end.

Target Market(s)

Wedding Couples

Contact Information for Business Card

Lewis Barnow Wedding Films
07312 580 417
films@lewisbarnow-example.com
www.lewisbarnow-example.com

Facebook: @lewisbarnowweddingfilms
Instagram: @lewisbarnowfilms

Font styles to use
Sans Serif

Requirements
Must have
• Social media icons - Facebook and Instagram

```html
<!DOCTYPE html>
<html lang="en">
<head>
<meta charset="utf-8">
<title>Lewis Barnow Wedding Films – Business Card</title>
<link rel="stylesheet" href="https://fonts.googleapis.com/css2?family=Jost:wght@400;500&family=Quicksand:wght@400;500&display=swap">
<style>
  :root {
    --backdrop: #5a5b5e;
    --card: #ffffff;
    --ink: #2f3035;
    --band: #313238;
    --gold: #9c8a55;
    --on-dark: #ffffff;
  }
  * { margin: 0; padding: 0; box-sizing: border-box; }
  html, body { width: 1200px; height: 965px; overflow: hidden; }
  body {
    background: var(--backdrop);
    display: flex; flex-direction: column; align-items: center; justify-content: center;
    gap: 44px;
    font-family: "Quicksand", sans-serif;
  }
  .card {
    position: relative;
    width: 640px; height: 366px;
    background: var(--card);
    overflow: hidden;
    box-shadow: 0 6px 18px rgba(0,0,0,.35);
  }
  .wordmark {
    display: flex; align-items: center; gap: 16px;
    font-family: "Jost", sans-serif; font-weight: 500; color: var(--ink);
  }
  .wordmark__square { background: var(--ink); flex: none; }
  .wordmark__name { text-transform: uppercase; line-height: 1; }
  .wordmark__main { display: block; }
  .wordmark__sub { display: block; }

  .card--front { display: flex; align-items: center; justify-content: center; }
  .card--front .wordmark__square { width: 58px; height: 58px; }
  .card--front .wordmark__main { font-size: 38px; letter-spacing: 6px; }
  .card--front .wordmark__sub { font-size: 15px; letter-spacing: 9px; margin-top: 8px; padding-left: 60px; }

  .card--back .wordmark { position: absolute; top: 42px; right: 34px; gap: 10px; }
  .card--back .wordmark__square { width: 32px; height: 32px; }
  .card--back .wordmark__main { font-size: 21px; letter-spacing: 3px; }
  .card--back .wordmark__sub { font-size: 9px; letter-spacing: 5px; margin-top: 5px; padding-left: 34px; }

  .bands { position: absolute; inset: 0; }
  .holder { position: absolute; left: 34px; top: 196px; color: var(--ink); }
  .holder__name { font-family: "Jost", sans-serif; font-weight: 400; font-size: 24px; letter-spacing: 3px; text-transform: uppercase; line-height: 1; }
  .holder__role { font-size: 14px; margin-top: 4px; }

  .contacts { position: absolute; left: 34px; top: 288px; list-style: none; color: var(--on-dark); font-size: 14px; }
  .contacts li { display: flex; align-items: center; gap: 10px; height: 22px; }
  .contacts svg { width: 14px; height: 14px; flex: none; }

  .socials { position: absolute; right: 18px; top: 232px; list-style: none; color: var(--on-dark); font-size: 13px; text-align: right; }
  .socials li { display: flex; align-items: center; justify-content: flex-end; gap: 7px; height: 17px; }
  .socials__mark { width: 11px; height: 11px; background: var(--on-dark); border-radius: 2px; }
</style>
</head>
<body>
  <section class="card card--front">
    <div class="wordmark">
      <span class="wordmark__square"></span>
      <span class="wordmark__name">
        <span class="wordmark__main">Lewis Barnow</span>
        <span class="wordmark__sub">Wedding Films</span>
      </span>
    </div>
  </section>

  <section class="card card--back">
    <svg class="bands" viewBox="0 0 640 366" aria-hidden="true">
      <polygon points="0,284 318,284 340,234 640,234 640,366 0,366" fill="var(--band)"/>
      <polygon points="340,224 640,224 640,272 420,272" fill="var(--gold)" stroke="#ffffff" stroke-width="3"/>
    </svg>

    <div class="wordmark">
      <span class="wordmark__square"></span>
      <span class="wordmark__name">
        <span class="wordmark__main">Lewis Barnow</span>
        <span class="wordmark__sub">Wedding Films</span>
      </span>
    </div>

    <div class="holder">
      <p class="holder__name">Lewis Barnow</p>
      <p class="holder__role">CEO/ Owner</p>
    </div>

    <ul class="contacts">
      <li>
        <svg viewBox="0 0 16 16" fill="none" stroke="currentColor" stroke-width="1.4"><path d="M4 1.5h2.5l1 3.5-1.8 1.2a8 8 0 0 0 4.1 4.1L11 8.5l3.5 1V12a2 2 0 0 1-2 2A11 11 0 0 1 2 3.5a2 2 0 0 1 2-2z"/></svg>
        07312 580 417
      </li>
      <li>
        <svg viewBox="0 0 16 16" fill="none" stroke="currentColor" stroke-width="1.4"><rect x="1.5" y="3.5" width="13" height="9"/><path d="M1.5 3.5 8 9l6.5-5.5"/></svg>
        films@lewisbarnow-example.com
      </li>
      <li>
        <svg viewBox="0 0 16 16" fill="none" stroke="currentColor" stroke-width="1.4"><circle cx="8" cy="8" r="6.5"/><ellipse cx="8" cy="8" rx="2.8" ry="6.5"/><path d="M1.5 8h13"/></svg>
        www.lewisbarnow-example.com
      </li>
    </ul>

    <ul class="socials">
      <li>@lewisbarnowweddingfilms <span class="socials__mark"></span></li>
      <li>@lewisbarnowfilms <span class="socials__mark"></span></li>
    </ul>
  </section>
</body>
</html>
```